Financial Advisor needs a BOLD Business Card

I need a business card that is professional, and is also eye-catching and memorable. I would like to include my photo (several different professional photos have been uploaded). Preferred primary color is blue, or green, or dark purple. The final design should have a modern/contemporary look while communicating a professional image.

Target Market(s)

Individual Investors and Small Business Owners

Industry/Entity Type

Business

Contact Information for Business Card

[side 1:] Dale Varkonen Financial Advisor 58217 Marlow Brook Rd., #240 St. Louis, MO 63975 (314) 555-0187 main (314) 555-0142 cell (314) 555-0169 fax dalev@qrmvbk.com [side 2:] Life Insurance | Retirement | Employee Benefits

Font styles to use
Serif
Sans Serif

Requirements
Must have
• [disclaimer, text can be 7-9 point:] Securities offered through the K.R. Capital Trading Company. Member BLUDA/TAVK. Nine Harbor Circle, Cincinnati, Ohio 45817. 513-555-0123. Investment Advisory Services offered through K.R. Portfolio Stewardship Company.
Nice to have
• Bright, Light & Airy feel on Side 1 with contact data, bold patterns, high color contrast, modern or 3D look
Should not have
• Any symbols referring to money (e.g. $)

```html
<!DOCTYPE html>
<html lang="en">
<head>
<meta charset="utf-8">
<title>Dale Varkonen – Business Card</title>
<link rel="stylesheet" href="https://fonts.googleapis.com/css2?family=Josefin+Sans:wght@400;600&family=Roboto+Condensed:wght@400;500&family=Source+Sans+3:wght@400;600;700&display=swap">
<style>
  :root {
    --page: #ffffff;
    --navy-deep: #0d1330;
    --navy-band: rgba(18, 20, 62, 0.88);
    --ink-box: rgba(8, 10, 32, 0.86);
    --suit-dark: #1b2233;
    --suit-mid: #2e3a55;
    --suit-light: #3c4a68;
    --portrait-grey: #4a505c;
    --portrait-dark: #2a2e38;
    --bokeh-green: #4d5a3e;
    --bokeh-brick: #6a4a46;
    --white: #ffffff;
  }
  * { margin: 0; padding: 0; box-sizing: border-box; }
  html, body { width: 1200px; height: 927px; overflow: hidden; background: var(--page); }
  .canvas { position: relative; width: 1200px; height: 927px; }

  .card {
    position: absolute;
    top: 150px;
    width: 324px;
    height: 564px;
    overflow: hidden;
    color: var(--white);
    box-shadow: 4px 6px 10px rgba(0, 0, 0, 0.35);
  }
  .card--front { left: 236px; }
  .card--back { left: 602px; }

  .photo { position: absolute; inset: 0; }
  .photo--suit {
    background: linear-gradient(180deg, var(--suit-light) 0%, var(--suit-mid) 45%, var(--suit-dark) 100%);
  }
  .photo--scene {
    background: linear-gradient(90deg, var(--bokeh-brick) 0%, #3b2f33 30%, var(--bokeh-green) 65%, #8a8f86 100%);
  }
  .portrait {
    position: absolute;
    left: 6px; right: 6px;
    top: 138px;
    bottom: 0;
    border-radius: 150px 150px 0 0;
    background: linear-gradient(180deg, var(--portrait-grey) 0%, var(--portrait-dark) 100%);
  }

  .name-band {
    position: absolute;
    left: 0; right: 0;
    top: 80px;
    height: 93px;
    background: var(--navy-band);
    text-align: center;
  }
  .name {
    font-family: "Josefin Sans", sans-serif;
    font-weight: 400;
    font-size: 27px;
    letter-spacing: 1.5px;
    text-transform: uppercase;
    padding-top: 22px;
    line-height: 1;
  }
  .title {
    font-family: "Source Sans 3", sans-serif;
    font-size: 18px;
    margin-top: 10px;
  }

  .contact {
    position: absolute;
    left: 52px; right: 0;
    top: 282px;
    height: 168px;
    background: var(--ink-box);
    padding: 22px 28px 0 0;
    list-style: none;
    text-align: right;
    font-family: "Source Sans 3", sans-serif;
    font-size: 23px;
    line-height: 29.5px;
  }
  .contact__label { font-weight: 700; margin-right: 4px; }

  .services {
    position: absolute;
    left: 0; right: 0;
    top: 0;
    height: 112px;
    background: linear-gradient(180deg, var(--navy-deep) 0%, rgba(13, 19, 48, 0.88) 75%, rgba(13, 19, 48, 0) 100%);
    padding: 22px 30px 0 0;
    list-style: none;
    text-align: right;
    font-family: "Source Sans 3", sans-serif;
    font-size: 19px;
    line-height: 27px;
  }

  .disclaimer {
    position: absolute;
    left: 0; right: 0; bottom: 0;
    height: 124px;
    background: var(--ink-box);
    padding: 14px 14px 0 23px;
    font-family: "Roboto Condensed", sans-serif;
    font-weight: 500;
    font-size: 12.5px;
    line-height: 18.5px;
  }
</style>
</head>
<body>
<main class="canvas">
  <section class="card card--front">
    <div class="photo photo--suit" role="img" aria-label="Close-up photo of a pinstripe suit with white shirt and bright blue patterned tie"></div>
    <header class="name-band">
      <h1 class="name">Dale Varkonen</h1>
      <p class="title">Financial Advisor</p>
    </header>
    <ul class="contact">
      <li><span class="contact__label">o</span> 314.555.0187</li>
      <li><span class="contact__label">c</span> 314.555.0142</li>
      <li><span class="contact__label">f</span> 314.555.0169</li>
      <li>dalev@qrmvbk.com</li>
    </ul>
  </section>

  <section class="card card--back">
    <div class="photo photo--scene" role="img" aria-label="Softly blurred outdoor background of brick and greenery"></div>
    <div class="portrait" role="img" aria-label="Portrait photo of the financial advisor in a grey suit and blue tie"></div>
    <ul class="services">
      <li>Life Insurance</li>
      <li>Retirement</li>
      <li>Employee Benefits</li>
    </ul>
    <p class="disclaimer">Securities offered through the K.R. Capital Trading Company. Member BLUDA/TAVK. Nine Harbor Circle, Cincinnati, Ohio 45817. 513-555-0123. Investment Advisory Services offered through K.R. Portfolio Stewardship Company.</p>
  </section>
</main>
</body>
</html>
```